Corporate Website - KWARTA HOLDINGS, LLC

This Nevada Corporation has several subsidiaries:
T. M. Designs - Interior Design; Commercial, Residential & Hospitality
T. M. Style - Fashion Design & Styling
FERN LOUNGE - Upscale Membership Only Lounge servicing Business Men and women. It is located in Accra, Ghana
FERN SUITES - Full Service Executive Suites for top Businesses. Located in Accra, Ghana.
THE MATERIAL YARD - Distributor for Building and Interior Design Materials
URL: www.kwartaholdingsllc.example
Website: info@kwartaholdingsllc.example
Phones: 1 702-555-0147 Las Vegas; +233 26 5550193 Ghana

Industry/Entity Type

Fashion

```html
<!DOCTYPE html>
<html lang="en">
<head>
<meta charset="utf-8">
<title>Kwarta Holdings, LLC — Building and Interior Design Materials Marketplace</title>
<link href="https://fonts.googleapis.com/css2?family=Montserrat:wght@300;400;600;700&family=Open+Sans:wght@400;600;700&display=swap" rel="stylesheet">
<style>
:root{
  --navy:#2b3a4b;
  --hero-top:#3a8fd0;
  --hero-bottom:#2a74b5;
  --accent:#3d9ae0;
  --gold:#f4b301;
  --text:#333b44;
  --muted:#7a8490;
  --line:#e6e8eb;
  --band:#f2f2f2;
  --white:#ffffff;
}
*{box-sizing:border-box;margin:0;padding:0}
html,body{width:1200px;height:2341px;overflow:hidden}
body{position:relative;font-family:"Open Sans",Arial,sans-serif;color:var(--text);background:var(--white)}
.abs{position:absolute}

/* header */
.site-header{position:absolute;left:0;top:0;width:1200px;height:88px;background:var(--navy)}
.brand{left:160px;top:30px;font-family:"Montserrat",sans-serif;font-weight:700;font-size:18px;color:var(--white);white-space:nowrap}
.main-nav{left:0;top:0;width:1200px;height:88px;font-family:"Montserrat",sans-serif;font-size:11px;color:var(--white)}
.main-nav a{position:absolute;top:38px;color:var(--white);text-decoration:none;white-space:nowrap}
.main-nav a.active{color:var(--accent)}
.login-btn{left:837px;top:30px;width:127px;height:28px;background:var(--accent);color:var(--white);border-radius:3px;font-family:"Montserrat",sans-serif;font-size:11px;display:flex;align-items:center;justify-content:center;white-space:nowrap}
.header-icon{top:35px}

/* hero */
.hero{position:absolute;left:0;top:88px;width:1200px;height:575px;background:linear-gradient(180deg,var(--hero-top),var(--hero-bottom))}
.hero-title{top:30px;left:0;width:1200px;text-align:center;font-family:"Montserrat",sans-serif;font-weight:300;font-size:30px;color:var(--white)}
.hero-title strong{font-weight:700}
.hero-lead{top:80px;left:240px;width:720px;text-align:center;font-size:13px;line-height:21px;color:var(--white)}
.hero-video{left:310px;top:146px;width:580px;height:362px;background:linear-gradient(160deg,#6b6258,#a89a86 45%,#8e8a84 75%,#5b544d);border:2px solid rgba(255,255,255,.25)}
.play{left:254px;top:145px}
.shop-btn{left:546px;top:521px;width:100px;height:33px;background:var(--gold);color:var(--white);font-family:"Montserrat",sans-serif;font-weight:700;font-size:12px;display:flex;align-items:center;justify-content:center;border-radius:2px}

/* latest products */
.products-intro{left:160px;top:697px;width:200px}
.section-kicker{font-family:"Montserrat",sans-serif;font-size:18px;color:var(--text)}
.section-sub{font-family:"Montserrat",sans-serif;font-weight:700;font-size:14px;color:var(--text);margin-top:4px}
.products-intro p{margin-top:22px;font-size:12px;line-height:20px;color:#555}
.arrow{width:26px;height:26px;display:flex;align-items:center;justify-content:center;border-radius:2px}
.arrow.off{background:#e3e5e8}
.arrow.on{background:var(--accent)}
.tile{top:700px;width:203px;height:201px}
.tile-marble{left:386px;background:linear-gradient(180deg,#5ea7e0,#4d97d4)}
.tile-marble .label{position:absolute;top:80px;width:100%;text-align:center;color:var(--white);font-size:12px}
.tile-marble .btn{position:absolute;left:63px;top:101px;width:77px;height:20px;border:1px solid var(--white);color:var(--white);font-size:10px;display:flex;align-items:center;justify-content:center}
.tile-house{left:611px;background:linear-gradient(180deg,#2c3b2f,#6b6a52 55%,#c4a974)}
.tile-wood{left:835px;background:linear-gradient(135deg,#b9713a,#d29459 50%,#a6602e)}

/* featured */
.featured{position:absolute;left:0;top:940px;width:1200px;height:488px;background:var(--band)}
.featured-head{left:160px;top:34px}
.featured-head .section-sub{font-size:13px}
.featured-arrows{left:985px;top:43px;display:flex;gap:3px}
.featured-photo{left:160px;top:98px;width:353px;height:351px;border:10px solid var(--accent);background:linear-gradient(180deg,#8a9aa8 0%,#b4b0a6 30%,#c7a57c 45%,#b88a5f 100%)}
.featured-body{left:536px;top:96px;width:500px}
.featured-body h2{font-family:"Montserrat",sans-serif;font-weight:600;font-size:21px;color:var(--text)}
.by{margin-top:8px;font-size:12px;color:var(--text)}
.by span{color:var(--accent);font-weight:700}
.featured-body p{margin-top:10px;font-size:12px;line-height:19px;color:#666}
.featured-body p + p{margin-top:18px}
.outline-btn{margin-top:24px;width:104px;height:28px;border:1px solid #777;font-size:12px;display:flex;align-items:center;justify-content:center;color:#555;background:var(--white)}

/* news & blog */
.feed{top:1462px;width:416px}
.feed-news{left:160px}
.feed-blog{left:620px}
.feed .section-kicker{font-size:17px}
.feed .section-sub{font-size:17px;margin-top:0}
.feed-list{list-style:none;margin-top:28px}
.feed-item{display:flex;height:98px;border-bottom:1px solid var(--line);padding-top:0}
.feed-item + .feed-item{padding-top:0}
.thumb{width:68px;height:68px;flex:none}
.feed-text{margin-left:22px}
.feed-text h3{font-size:13px;font-weight:700;color:var(--text);font-family:"Open Sans",sans-serif}
.feed-text .cat{font-size:11px;color:var(--muted);margin-top:3px}
.feed-text .date{font-size:11px;color:var(--muted);margin-top:9px}
.divider{left:601px;top:1462px;width:1px;height:600px;background:var(--line)}
.pager{display:flex;gap:4px;top:2039px}
.pager span{height:22px;min-width:21px;padding:0 6px;background:#e9ebee;font-size:11px;display:flex;align-items:center;justify-content:center;color:#555}
.pager span.current{background:var(--accent);color:var(--white)}

/* footer */
.site-footer{position:absolute;left:0;top:2097px;width:1200px;height:244px;background:var(--navy)}
.contact{display:flex;align-items:center;top:40px}
.contact .badge{width:46px;height:46px;border-radius:50%;display:flex;align-items:center;justify-content:center;flex:none}
.contact .txt{margin-left:14px;font-size:11px;line-height:18px;color:var(--white);white-space:nowrap}
.footer-nav{top:114px;left:0;width:1200px;display:flex;justify-content:center;gap:24px;font-family:"Montserrat",sans-serif;font-size:11px;color:var(--white)}
.socials{top:150px;left:0;width:1200px;display:flex;justify-content:center;gap:12px}
.socials span{width:30px;height:30px;border-radius:50%}
.copyright{top:200px;left:0;width:1200px;text-align:center;font-size:10px;color:var(--white)}
</style>
</head>
<body>

<header class="site-header">
  <div class="abs brand">Kwarta Holdings, LLC.</div>
  <nav class="abs main-nav">
    <a class="active" style="left:406px">HOME</a>
    <a style="left:464px">PRODUCTS</a>
    <a style="left:552px">COLLECTION</a>
    <a style="left:648px">WHAT'S NEW</a>
    <a style="left:745px">CONTACT US</a>
  </nav>
  <div class="abs login-btn">LOGIN &nbsp;|&nbsp; REGISTER</div>
  <svg class="abs header-icon" style="left:990px" width="18" height="18" viewBox="0 0 18 18" fill="none" stroke="#fff" stroke-width="1.6"><path d="M1 2h3l2 9h9l2-6H5"/><circle cx="7" cy="15" r="1.3" fill="#fff"/><circle cx="14" cy="15" r="1.3" fill="#fff"/></svg>
  <svg class="abs header-icon" style="left:1024px" width="18" height="18" viewBox="0 0 18 18" fill="none" stroke="#fff" stroke-width="1.8"><circle cx="7" cy="7" r="5"/><path d="M11 11l5 5"/></svg>
</header>

<section class="hero">
  <h1 class="abs hero-title">The world's #1 Building and Interior Design Materials <strong>Marketplace</strong></h1>
  <p class="abs hero-lead">Lorem ipsum dolor sit amet, consectetur adipiscing elit, sed do eiusmod tempor incididunt ut labore et dolore magna aliqua. Ut enim ad minim veniam, quis nostrud exercitation ullamco laboris nisi ut aliquip.</p>
  <div class="abs hero-video" role="img" aria-label="Video still of a restaurant and bar interior with wooden stools and tiled floor">
    <svg class="abs play" width="72" height="72" viewBox="0 0 72 72"><circle cx="36" cy="36" r="33" fill="rgba(0,0,0,.25)" stroke="#fff" stroke-width="3"/><path d="M29 22l22 14-22 14z" fill="#fff"/></svg>
  </div>
  <div class="abs shop-btn">SHOP NOW</div>
</section>

<section>
  <div class="abs products-intro">
    <div class="section-kicker">Latest Products</div>
    <div class="section-sub">KWARTA HOLDINGS, LLC</div>
    <p>Lorem ipsum dolor sit amet, consectetur adipiscing elit, sed do eiusmod tempor incididunt ut labore et dolore magna aliqua.</p>
  </div>
  <div class="abs arrow off" style="left:160px;top:874px"><svg width="8" height="12" viewBox="0 0 8 12"><path d="M6 1L1 6l5 5" stroke="#fff" stroke-width="2" fill="none"/></svg></div>
  <div class="abs arrow on" style="left:190px;top:874px"><svg width="8" height="12" viewBox="0 0 8 12"><path d="M2 1l5 5-5 5" stroke="#fff" stroke-width="2" fill="none"/></svg></div>
  <div class="abs tile tile-marble" role="img" aria-label="Marble effect flooring in a lounge, shown under a blue overlay">
    <div class="label">Marble Effect</div>
    <div class="btn">More Details</div>
  </div>
  <div class="abs tile tile-house" role="img" aria-label="Modern house with lit glass walls at dusk"></div>
  <div class="abs tile tile-wood" role="img" aria-label="Close-up of wood grain with a knot"></div>
</section>

<section class="featured">
  <div class="abs featured-head">
    <div class="section-kicker">Featured</div>
    <div class="section-sub">Products Of The Month</div>
  </div>
  <div class="abs featured-arrows">
    <div class="arrow off"><svg width="8" height="12" viewBox="0 0 8 12"><path d="M6 1L1 6l5 5" stroke="#fff" stroke-width="2" fill="none"/></svg></div>
    <div class="arrow on"><svg width="8" height="12" viewBox="0 0 8 12"><path d="M2 1l5 5-5 5" stroke="#fff" stroke-width="2" fill="none"/></svg></div>
  </div>
  <div class="abs featured-photo" role="img" aria-label="Pool terrace with wooden deck tiles in front of a hillside apartment building"></div>
  <div class="abs featured-body">
    <h2>Villa Terrazza Private Residences</h2>
    <div class="by">Products By <span>Kwarta Holdings, LLC</span></div>
    <p>Proin condimentum fermentum nunc. Etiam pharetra, erat sed fermentum Proin condimentum fermentum Etiam pharetra, erat sed fermentum pendisse in orci enim.Proin condimentum fermentum nunc.Proin condimentum fermentum nunc.</p>
    <p>Sed ut perspiciatis unde omnis iste natus error sit voluptatem accusantium doloremque laudantium, totam rem aperiam, eaque ipsa quae ab illo inventore veritatis et quasi architecto beatae vitae dicta sunt explicabo. Nemo enim ipsam voluptatem quia voluptas sit aspernatur aut odit aut fugit, sed quia consequuntur magni dolores eos qui ratione voluptatem sequi nesciunt.</p>
    <p>Neque porro quisquam est, qui dolorem ipsum quia dolor sit amet, consectetur, adipisci velit, sed quia non numquam eius modi tempora incidunt ut labore et dolore magnam aliquam quaerat voluptatem.</p>
    <div class="outline-btn">More Details</div>
  </div>
</section>

<section>
  <div class="abs feed feed-news">
    <div class="section-kicker">Latest</div>
    <div class="section-sub">News</div>
    <ul class="feed-list">
      <li class="feed-item"><div class="thumb" style="background:linear-gradient(135deg,#cfd3d6,#6d6a66)" role="img" aria-label="Office desk by a window"></div><div class="feed-text"><h3>Lorem ipsum dolor sit amet dosis litusdes</h3><div class="cat">Interior Design</div><div class="date">20 Feb 2015</div></div></li>
      <li class="feed-item"><div class="thumb" style="background:linear-gradient(180deg,#8fa27e,#e7e5de)" role="img" aria-label="Bright dining room with green chairs"></div><div class="feed-text"><h3>Lorem ipsum dolor sit amet dosis litusdes</h3><div class="cat">Interior Design</div><div class="date">15 Jan 2015</div></div></li>
      <li class="feed-item"><div class="thumb" style="background:linear-gradient(135deg,#5f7a5a,#e8e6e0)" role="img" aria-label="Dining area opening onto a garden"></div><div class="feed-text"><h3>Lorem ipsum dolor sit amet dosis litusdes</h3><div class="cat">Interior Design</div><div class="date">15 Jan 2015</div></div></li>
      <li class="feed-item"><div class="thumb" style="background:linear-gradient(180deg,#f1f1f0,#3a3a3a)" role="img" aria-label="White room with a dark side table"></div><div class="feed-text"><h3>Lorem ipsum dolor sit amet dosis litusdes</h3><div class="cat">Interior Design</div><div class="date">10 Jan 2015</div></div></li>
      <li class="feed-item"><div class="thumb" style="background:linear-gradient(135deg,#3b2a22,#8a6a52)" role="img" aria-label="Dark living room with leather sofa"></div><div class="feed-text"><h3>Lorem ipsum dolor sit amet dosis litusdes</h3><div class="cat">Interior Design</div><div class="date">15 Jan 2015</div></div></li>
    </ul>
  </div>
  <div class="abs divider"></div>
  <div class="abs feed feed-blog">
    <div class="section-kicker">Latest</div>
    <div class="section-sub">Blog</div>
    <ul class="feed-list">
      <li class="feed-item"><div class="thumb" style="background:linear-gradient(180deg,#6f8b6a,#e4e2dc)" role="img" aria-label="Conference room with glass wall"></div><div class="feed-text"><h3>Lorem ipsum dolor sit amet dosis litusdes</h3><div class="cat">Commercial</div><div class="date">10 Jan 2015</div></div></li>
      <li class="feed-item"><div class="thumb" style="background:linear-gradient(180deg,#f0efec,#4a4440)" role="img" aria-label="Bright room with a dark chair"></div><div class="feed-text"><h3>Lorem ipsum dolor sit amet dosis litusdes</h3><div class="cat">Commercial</div><div class="date">15 Jan 2015</div></div></li>
      <li class="feed-item"><div class="thumb" style="background:linear-gradient(135deg,#5f7a5a,#e8e6e0)" role="img" aria-label="Dining area opening onto a garden"></div><div class="feed-text"><h3>Lorem ipsum dolor sit amet dosis litusdes</h3><div class="cat">Commercial</div><div class="date">20 Apr 2015</div></div></li>
      <li class="feed-item"><div class="thumb" style="background:linear-gradient(135deg,#3b2a22,#8a6a52)" role="img" aria-label="Dark living room with leather sofa"></div><div class="feed-text"><h3>Lorem ipsum dolor sit amet dosis litusdes</h3><div class="cat">Commercial</div><div class="date">15 Jan 2015</div></div></li>
      <li class="feed-item"><div class="thumb" style="background:linear-gradient(180deg,#e9e7e3,#7b7068)" role="img" aria-label="Minimal lounge with a low table"></div><div class="feed-text"><h3>Lorem ipsum dolor sit amet dosis litusdes</h3><div class="cat">Commercial</div><div class="date">20 Jan 2014</div></div></li>
    </ul>
  </div>
  <div class="abs pager" style="left:312px"><span class="current">1</span><span>2</span><span>3</span><span>Next</span></div>
  <div class="abs pager" style="left:774px"><span class="current">1</span><span>2</span><span>3</span><span>Next</span></div>
</section>

<footer class="site-footer">
  <div class="abs contact" style="left:160px">
    <div class="badge" style="background:#5fc5a6"><svg width="18" height="24" viewBox="0 0 18 24"><path d="M9 1a8 8 0 0 0-8 8c0 6 8 14 8 14s8-8 8-14a8 8 0 0 0-8-8z" fill="#fff"/><circle cx="9" cy="9" r="3" fill="#5fc5a6"/></svg></div>
    <div class="txt">1332 Lorem Ipsum,<br>Accra, Ghana</div>
  </div>
  <div class="abs contact" style="left:476px">
    <div class="badge" style="background:#4da3e0"><svg width="22" height="22" viewBox="0 0 24 24"><path d="M6.6 10.8a15 15 0 0 0 6.6 6.6l2.2-2.2c.3-.3.7-.4 1-.2 1.1.4 2.3.6 3.6.6.6 0 1 .4 1 1V20c0 .6-.4 1-1 1A17 17 0 0 1 3 4c0-.6.4-1 1-1h3.5c.6 0 1 .4 1 1 0 1.3.2 2.5.6 3.6.1.3 0 .7-.2 1z" fill="#fff"/></svg></div>
    <div class="txt">Give us a call<br>(01) 702-555-0147 / (+233) 26 5550193</div>
  </div>
  <div class="abs contact" style="left:831px">
    <div class="badge" style="background:#f0a45a"><svg width="22" height="16" viewBox="0 0 22 16"><rect x="1" y="1" width="20" height="14" rx="1" fill="#fff"/><path d="M1 2l10 7 10-7" stroke="#f0a45a" stroke-width="1.6" fill="none"/></svg></div>
    <div class="txt">Drop us a mail<br>info@kwartaholdingsllc.example</div>
  </div>
  <nav class="abs footer-nav"><span>HOME</span><span>PRODUCTS</span><span>COLLECTION</span><span>WHAT'S NEW</span><span>CONTACT US</span></nav>
  <div class="abs socials">
    <span style="background:#3aa4e6"></span><span style="background:#3b62b0"></span><span style="background:#dc4a38"></span>
  </div>
  <div class="abs copyright">Copyright © 2015 KWARTA HOLDINGS, LLC. All Rights Reserved.</div>
</footer>

</body>
</html>
```